Varnek Group Business Card

Varnek Group — Business Card Design Brief
Overview
Design a double-sided business card for Varnek Group that highlights our two service arms: Varnek Communications (telecommunications) and Varnek Energy (business energy solutions). The card should feel smart and stand out when handed to clients.

Objectives
Showcase our areas of specialty clearly.
Reflect the overall Varnek / Varnek Group brand while acknowledging both arms.
Explore using both logos (Communications + Energy) or one unified logo, depending on the design.

Deliverables
One double-sided business card design (front + back).

Content & Copy
Front (preferred): Logo: Varnek / Varnek Group
Descriptor: Business Communications | Business Energy
Back:My contact details and company details
Core products: Business Mobile • Telephony • Internet • Business Energy Solutions

Brand & Visual Direction
We have a group logo currently tailored more toward telecoms, plus a separate Varnek Energy logo.
Please explore layouts that use both logos or just one, whichever works best.
Color: I wouldn't mind seeing an option using our the Blue/Purple gradient from our website (varnek-example.co.uk), but also open to non-gradient approaches and other colours..

Overall look: Smart, modern, and distinctive.
Format & Print Specs
Double-sided business card format. (Use a standard size

Must-Haves
Front: Varnek wording or Varnek Group wording with atleast 1 logo also on front “Business Communications | Business Energy.”

Back: Contact + company details and core products.
A design that stands out while remaining professional.

Nice-to-Have Options
A gradient version using our site’s Blue/Purple gradient.
A non-gradient version.
A dual-logo treatment versus a single-logo treatment.

Thanks
Dominic

```html
<!DOCTYPE html>
<html lang="en">
<head>
<meta charset="utf-8">
<title>Varnek Group Business Card</title>
<link rel="stylesheet" href="https://fonts.googleapis.com/css2?family=Montserrat:wght@500;700;800&family=Open+Sans:wght@400;600&display=swap">
<style>
  :root {
    --stage: #1f1f21;
    --paper: #ffffff;
    --navy: #1c1a6b;
    --blue: #1f6fd1;
    --sky: #1ea3dc;
    --steel: #3462b8;
    --green: #4fb81c;
    --lime: #d6dc00;
    --ink: #1c1a6b;
  }
  * { box-sizing: border-box; margin: 0; padding: 0; }
  html, body { width: 1200px; height: 1200px; overflow: hidden; }
  body {
    background: var(--stage);
    position: relative;
    font-family: "Montserrat", sans-serif;
  }
  .card {
    position: absolute;
    left: 150px;
    width: 900px;
    height: 514px;
    background: var(--paper);
    overflow: hidden;
    box-shadow: 0 18px 40px rgba(0,0,0,.45);
  }
  .card--front { top: 62px; }
  .card--back  { top: 624px; }
  .card__art { position: absolute; inset: 0; width: 100%; height: 100%; }

  /* front */
  .front-brand {
    position: absolute;
    left: 0; right: 0; top: 120px;
    display: flex; flex-direction: column; align-items: center; gap: 26px;
  }
  .brand-dot {
    width: 96px; height: 96px; border-radius: 50%;
    background: var(--green);
  }
  .front-brand__name {
    font-weight: 800; font-size: 48px; letter-spacing: 3px; color: var(--navy);
  }
  .front-products {
    position: absolute; left: 0; right: 0; top: 462px;
    text-align: center;
    font-weight: 500; font-size: 19px; letter-spacing: 1px;
    color: var(--paper);
  }

  /* back */
  .contact {
    position: absolute; left: 78px; top: 168px;
    color: var(--ink);
  }
  .contact__name {
    font-weight: 700; font-size: 30px; letter-spacing: 1.5px; line-height: 1;
  }
  .contact__role {
    font-family: "Open Sans", sans-serif; font-weight: 400; font-size: 25px; margin-top: 4px;
  }
  .contact__rule {
    width: 170px; height: 4px; margin-top: 16px; border-radius: 2px;
    background: linear-gradient(90deg, var(--blue), var(--sky));
  }
  .contact__list { list-style: none; margin-top: 26px; }
  .contact__item {
    display: flex; align-items: center; gap: 14px;
    font-family: "Open Sans", sans-serif; font-size: 24px; line-height: 36px;
  }
  .contact__icon {
    width: 26px; height: 26px; border-radius: 50%;
    background: linear-gradient(135deg, var(--blue), var(--sky));
    display: flex; align-items: center; justify-content: center; flex: none;
  }
  .contact__icon svg { width: 16px; height: 16px; }
  .back-brand {
    position: absolute; left: 560px; top: 140px;
    display: flex; flex-direction: column; align-items: center; gap: 22px;
  }
  .back-brand .brand-dot { width: 110px; height: 110px; background: var(--blue); }
  .back-brand__name {
    font-weight: 800; font-size: 64px; letter-spacing: 3px; color: var(--navy);
  }
</style>
</head>
<body>

<section class="card card--front" aria-label="Card front">
  <svg class="card__art" viewBox="0 0 900 514" aria-hidden="true">
    <defs>
      <linearGradient id="greenBand" x1="0" y1="0" x2="1" y2="0">
        <stop offset="0" stop-color="#c9d400"/>
        <stop offset=".35" stop-color="#4fb81c"/>
        <stop offset=".75" stop-color="#5cbc18"/>
        <stop offset="1" stop-color="#d6dc00"/>
      </linearGradient>
    </defs>
    <path d="M0,352 C260,430 560,462 900,446 V514 H0 Z" fill="var(--navy)"/>
    <path d="M0,372 C260,450 560,480 900,464 V514 H0 Z" fill="url(#greenBand)"/>
  </svg>
  <div class="front-brand">
    <span class="brand-dot"></span>
    <span class="front-brand__name">VARNEK GROUP</span>
  </div>
  <p class="front-products">Business Mobile • Telephony • Internet • Business Energy Solutions</p>
</section>

<section class="card card--back" aria-label="Card back">
  <svg class="card__art" viewBox="0 0 900 514" aria-hidden="true">
    <defs>
      <linearGradient id="blueBand" x1="0" y1="0" x2="1" y2="0">
        <stop offset="0" stop-color="#3462b8"/>
        <stop offset=".6" stop-color="#2b78c9"/>
        <stop offset="1" stop-color="#1ea3dc"/>
      </linearGradient>
    </defs>
    <path d="M0,0 H200 C120,22 50,62 0,110 Z" fill="var(--steel)"/>
    <path d="M0,140 C130,62 340,22 580,18 C340,44 140,110 0,196 Z" fill="var(--navy)"/>
    <path d="M0,396 C300,456 620,488 900,468 V514 H0 Z" fill="var(--navy)"/>
    <path d="M0,414 C300,474 620,506 900,486 V514 H0 Z" fill="url(#blueBand)"/>
  </svg>

  <div class="contact">
    <h1 class="contact__name">MARCUS HALE</h1>
    <p class="contact__role">Business development manager</p>
    <div class="contact__rule"></div>
    <ul class="contact__list">
      <li class="contact__item">
        <span class="contact__icon"><svg viewBox="0 0 16 16"><path d="M4 2 L6 2 L7 5 L5.5 6.2 C6.3 8 8 9.7 9.8 10.5 L11 9 L14 10 L14 12 C14 13 13 14 12 14 C7 14 2 9 2 4 C2 3 3 2 4 2 Z" fill="#fff"/></svg></span>
        206-555-0148
      </li>
      <li class="contact__item">
        <span class="contact__icon"><svg viewBox="0 0 16 16"><rect x="2" y="4" width="12" height="8" rx="1" fill="#fff"/><path d="M2.5 4.5 L8 9 L13.5 4.5" stroke="var(--blue)" stroke-width="1.2" fill="none"/></svg></span>
        marcus@varnekmail-example.com
      </li>
      <li class="contact__item">
        <span class="contact__icon"><svg viewBox="0 0 16 16" fill="none" stroke="#fff" stroke-width="1.2"><circle cx="8" cy="8" r="5.5"/><ellipse cx="8" cy="8" rx="2.5" ry="5.5"/><path d="M2.5 8 H13.5"/></svg></span>
        www.varnekweb-example.com
      </li>
    </ul>
  </div>

  <div class="back-brand">
    <span class="brand-dot"></span>
    <span class="back-brand__name">VARNEK</span>
  </div>
</section>

</body>
</html>
```